Honey jar label for small US farm

My daughters have 6 beehives and will be producing 300-400 jars of honey this season that they plan to sell at the farmers' market.
We are looking for a label design for small honey jars.
Label size:  1.5 inches high and 3 inches wide.
The label will be a simple RECTANGLE (no special cut)
We would like a playful look but upscale enough. We don't think that flowers or bees add anything. We like cleaner looks but not cold.
Maybe one could also represent the 3 sisters somewhere on the label. As elegant stick figures maybe?
One could also imagine a design where the label is black and the text/images are white to add some dramatic effect. The jar lid is black.
The honey is raw, un-pasturized, straight from the beehive.

Target Market(s)
Farm stand, sold by the 3 sisters who are 11, 9 and 6
Industry/Entity Type
Food Production
Colors
Designer to choose colors to be used in the design.
Requirements
Must have
- Name (means three sisters in English): Clos Ardent
- What it is: Larchmere Raw Honey
- Net weight: 3.75oz (110ml)
- Location: Hollis Glen, MA
- Text on one of the sides: Sister to sister we will always be, a couple of nuts off the family tree!
- Note that the jar is an hexagon. See the attached STOCK photo.
- Therefore, a little more than 1 inch is on the front facing, and 0.75 inches on each sides.

Nice to have
- The design should be elegant (but not ornate), but clean. Inviting and fun.
- No need for bees or flowers which would not make it look upscale.
- No gold or "over the top" fancy. Modern but not cold.
- Remember that this is a honey brand for 3 young sisters. Something playful but upscale would work too.
- Not sure about color codes. We are quite happy staying in grey scales, but a little bit of colour might work too.

Should not have
- No UPC code needed

```html
<!DOCTYPE html>
<html lang="en">
<head>
<meta charset="UTF-8">
<title>Clos Ardent — Larchmere Raw Honey Label</title>
<link href="https://fonts.googleapis.com/css2?family=Cinzel:wght@400;700&family=Playfair+Display:wght@400;700&family=Montserrat:wght@400&display=swap" rel="stylesheet">
<style>
  :root {
    --canvas: #e4e4e4;
    --label: #232123;
    --hex: #2f2d2f;
    --ink: #ffffff;
    --ink-soft: #e9e9e9;
    --tab: #e2e2e2;
    --tab-ink: #1c1b1c;
    --rule: #bdbdbd;
  }
  * { margin: 0; padding: 0; box-sizing: border-box; }
  html, body { width: 1200px; height: 1200px; overflow: hidden; }
  body {
    background: radial-gradient(circle at 50% 45%, #f2f2f2 0%, var(--canvas) 70%);
    position: relative;
  }
  .label {
    position: absolute;
    left: 40px; top: 320px;
    width: 1120px; height: 559px;
    background: var(--label);
    overflow: hidden;
    color: var(--ink);
  }
  .hex-field {
    position: absolute;
    left: 0; right: 0; bottom: 0; height: 200px;
    background: linear-gradient(to bottom, rgba(47,45,47,0) 0%, var(--hex) 45%, var(--hex) 100%);
    opacity: .85;
  }
  .brand-tab {
    position: absolute;
    left: 470px; top: 0;
    width: 179px; height: 106px;
    background: var(--tab);
    border-radius: 0 0 14px 14px;
    clip-path: polygon(0 0, 100% 0, 100% 84%, 0 100%);
    display: flex; align-items: center; justify-content: center;
    padding-bottom: 14px;
  }
  .brand-tab span {
    font-family: "Cinzel", serif;
    font-weight: 700;
    font-size: 22px;
    color: var(--tab-ink);
    white-space: nowrap;
  }
  .product-title {
    position: absolute;
    left: 0; right: 0; top: 150px;
    text-align: center;
    font-family: "Cinzel", serif;
    font-weight: 400;
    font-size: 52px;
    line-height: 50px;
    color: var(--ink-soft);
  }
  .sisters-art {
    position: absolute;
    left: 410px; top: 276px;
    width: 300px; height: 283px;
    border-radius: 120px 120px 0 0;
    background: linear-gradient(to bottom, rgba(255,255,255,1) 0%, rgba(255,255,255,.95) 35%, rgba(255,255,255,.35) 80%, rgba(255,255,255,0) 100%);
  }
  .side-left {
    position: absolute;
    left: 20px; top: 146px;
    width: 240px;
    text-align: center;
    font-family: "Playfair Display", serif;
  }
  .brand-mark {
    display: flex; justify-content: center;
    margin-bottom: 22px;
  }
  .brand-mark .dot {
    width: 112px; height: 112px;
    border: 3px solid var(--ink);
    border-radius: 50%;
  }
  .motto { font-size: 20px; line-height: 25px; }
  .location { font-size: 23px; margin-top: 28px; }
  .nutrition {
    position: absolute;
    left: 820px; top: 152px;
    width: 270px;
    font-family: "Playfair Display", serif;
  }
  .nutrition h2 {
    font-weight: 700; font-size: 22px; text-align: center; word-spacing: 4px;
  }
  .nutrition .serving {
    font-size: 17px; line-height: 19px; text-align: center; margin-top: 4px;
  }
  .nutrition table {
    margin-top: 20px; border-collapse: collapse; font-size: 18px; line-height: 22.5px;
  }
  .nutrition td { padding: 0; }
  .nutrition td:first-child { width: 198px; }
  .net-weight {
    position: absolute;
    left: 0; right: 0; top: 496px;
    display: flex; align-items: center; gap: 18px;
    font-family: "Montserrat", sans-serif;
    font-size: 17px;
    color: var(--ink-soft);
  }
  .net-weight::before, .net-weight::after {
    content: ""; height: 1px; background: var(--rule); flex: 1;
  }
</style>
</head>
<body>
  <main class="label">
    <div class="hex-field" role="img" aria-label="Faint honeycomb hexagon pattern"></div>

    <div class="brand-tab"><span>Clos Ardent</span></div>

    <h1 class="product-title">Larchmere<br>Raw Honey</h1>

    <div class="sisters-art" role="img" aria-label="White silhouettes of three sisters fading downward"></div>

    <section class="side-left">
      <div class="brand-mark">
        <div class="dot"></div>
      </div>
      <p class="motto">Sister to sister we will<br>always be, a couple of<br>nuts off the family tree!</p>
      <p class="location">Hollis Glen, MA</p>
    </section>

    <section class="nutrition">
      <h2>Nutrition Information</h2>
      <p class="serving">17 Servings per 110ml<br>Average serve &nbsp;&nbsp;15g</p>
      <table>
        <tr><td>Energy</td><td>210kJ</td></tr>
        <tr><td>Protein</td><td>0.05g</td></tr>
        <tr><td>Fat, total</td><td>0g</td></tr>
        <tr><td>unsaturated</td><td>0g</td></tr>
        <tr><td>Carbohydrate</td><td>12.5g</td></tr>
        <tr><td>- sugars</td><td>12.4g</td></tr>
        <tr><td>Sodium</td><td>2.3mg</td></tr>
      </table>
    </section>

    <div class="net-weight">3.75oz (110ml)</div>
  </main>
</body>
</html>
```